Double sided customer happy holidays and thank you card

Create a simple holiday theme thank you and happy holidays card using white and red (CMYK 0.94.100.0) as the primary colors with a dash of green (CMYK 85.3.91.44) peppered in the color scheme.
1. draft for templates in portrait view using: 4x6, 5x7, 5.5x8.5, and 6x9 (templates guidelines with bleed, trim, and safe areas attached.
2. Make prominent use of the company logo and icons (attached).
3. Backside of the card is devoted to customer instructions (attached).
4. Frontside wording draft attached.
5. Signatures, Walter & Phoebe, should be in handwritten script.
6. Words should be in a super large font size so that print is easy to read for all customers.

```html
<!DOCTYPE html>
<html lang="en">
<head>
<meta charset="utf-8">
<title>Crumbwell Holiday Card – Front and Back</title>
<link href="https://fonts.googleapis.com/css2?family=Cormorant+SC:wght@500;700&family=Lato:wght@400;700&family=Oleo+Script:wght@400;700&family=Great+Vibes&display=swap" rel="stylesheet">
<style>
  :root {
    --page-bg: #ececec;
    --card-green: #0f4433;
    --card-green-light: #1d5a45;
    --panel-white: #ffffff;
    --holiday-red: #ef3b24;
    --text-green: #1a5a40;
    --body-text: #3d5c4f;
    --frame-gold: #c9a868;
  }
  * { margin: 0; padding: 0; box-sizing: border-box; }
  html, body {
    width: 750px; height: 1200px; overflow: hidden;
    background: var(--page-bg);
  }
  .sheet {
    width: 750px; height: 1200px;
    display: flex; flex-direction: column; align-items: center;
    justify-content: center; gap: 14px;
  }
  .card {
    position: relative;
    width: 390px; height: 585px;
    box-shadow: 0 4px 14px rgba(0,0,0,0.18);
  }
  .card__foliage {
    position: absolute; inset: 0;
    background:
      radial-gradient(circle at 20% 15%, rgba(184,150,84,0.35), transparent 35%),
      radial-gradient(circle at 85% 80%, rgba(184,150,84,0.3), transparent 40%),
      linear-gradient(135deg, var(--card-green-light), var(--card-green));
  }
  .card__panel {
    position: absolute; top: 30px; left: 28px; right: 28px; bottom: 30px;
    background: var(--panel-white);
    padding: 6px;
  }
  .card__frame {
    width: 100%; height: 100%;
    border: 1px solid var(--frame-gold);
    display: flex; flex-direction: column; align-items: center;
    text-align: center;
    padding: 30px 24px 22px;
  }

  .brand-name {
    font-family: "Lato", sans-serif; font-weight: 400;
    color: var(--text-green);
    font-size: 22px; letter-spacing: 2px; line-height: 1;
    text-transform: uppercase;
  }
  .brand-name--large { font-size: 30px; letter-spacing: 3px; margin-top: 4px; }

  .greeting {
    font-family: "Oleo Script", cursive; font-weight: 400;
    color: var(--holiday-red);
    line-height: 0.92; margin-top: 26px;
  }
  .greeting__happy { font-size: 40px; display: block; }
  .greeting__holidays { font-size: 60px; display: block; }

  .smallcaps {
    font-family: "Cormorant SC", serif; font-weight: 700;
    color: var(--text-green); font-size: 15px; letter-spacing: 0.8px;
  }
  .accent { color: var(--holiday-red); }

  .from-line { margin-top: 10px; }

  .message {
    font-family: "Lato", sans-serif; font-size: 12.5px; line-height: 1.6;
    color: var(--body-text); margin-top: 26px;
  }
  .cheers { margin-top: auto; font-size: 14px; }
  .signature {
    font-family: "Great Vibes", cursive; color: var(--text-green);
    font-size: 38px; line-height: 1.1; margin-top: 4px;
  }

  .back-title { font-size: 15px; line-height: 1.1; }
  .tagline { font-size: 12px; margin-top: 6px; letter-spacing: 1px; }

  .care-list {
    list-style: none; margin-top: 16px; text-align: left;
    flex: 1;
    display: flex; flex-direction: column; justify-content: space-evenly;
  }
  .care-item { display: flex; gap: 12px; align-items: flex-start; }
  .care-item__icon { flex: 0 0 26px; width: 26px; height: 26px; }
  .care-item__text {
    font-family: "Lato", sans-serif; font-size: 10.5px; line-height: 1.5;
    color: var(--body-text);
  }
  .closing {
    margin-top: 10px;
    font-family: "Great Vibes", cursive; color: var(--text-green);
    font-size: 25px;
  }
</style>
</head>
<body>
<main class="sheet">

  <section class="card card--front">
    <div class="card__foliage" role="img" aria-label="Deep green background with gold leaf and branch pattern"></div>
    <div class="card__panel">
      <div class="card__frame">
        <p class="brand-name">Crumbwell</p>
        <h1 class="greeting">
          <span class="greeting__happy">Happy</span>
          <span class="greeting__holidays">Holidays</span>
        </h1>
        <p class="smallcaps from-line">From the <span class="accent">Crumbwell</span> Family!</p>
        <p class="message">We are so thankful for the chance to be a gift on your table this holiday season, although not for long, we are sure! Thanks for letting us be a part of your moments this year. We wish you the happiest of holidays and a bright New Year!</p>
        <p class="smallcaps cheers">Cheers to the holidays</p>
        <p class="signature">Walter &amp; Phoebe</p>
      </div>
    </div>
  </section>

  <section class="card card--back">
    <div class="card__foliage" role="img" aria-label="Deep green background with gold leaf and branch pattern"></div>
    <div class="card__panel">
      <div class="card__frame">
        <p class="smallcaps back-title">Getting the <span class="accent">most out</span> of your</p>
        <p class="brand-name brand-name--large">Crumbwell</p>
        <p class="smallcaps tagline">Care, Storage and Enjoyment</p>

        <ul class="care-list">
          <li class="care-item">
            <svg class="care-item__icon" viewBox="0 0 26 26" aria-hidden="true">
              <circle cx="13" cy="13" r="12" fill="none" stroke="#ef3b24" stroke-width="1.2"/>
              <rect x="9" y="6" width="8" height="14" rx="1.5" fill="none" stroke="#ef3b24" stroke-width="1.2"/>
              <line x1="9" y1="11" x2="17" y2="11" stroke="#ef3b24" stroke-width="1.2"/>
            </svg>
            <p class="care-item__text">Please refrigerate your cake as soon as it arrives and keep it in its sealed wrap until serving.</p>
          </li>
          <li class="care-item">
            <svg class="care-item__icon" viewBox="0 0 26 26" aria-hidden="true">
              <circle cx="13" cy="13" r="12" fill="none" stroke="#ef3b24" stroke-width="1.2"/>
              <circle cx="13" cy="13" r="6" fill="none" stroke="#ef3b24" stroke-width="1.2"/>
              <polyline points="13,9.5 13,13 15.5,14.5" fill="none" stroke="#ef3b24" stroke-width="1.2"/>
            </svg>
            <p class="care-item__text">Let it rest at room temperature for about thirty minutes before slicing for the softest crumb and the richest flavor.</p>
          </li>
          <li class="care-item">
            <svg class="care-item__icon" viewBox="0 0 26 26" aria-hidden="true">
              <circle cx="13" cy="13" r="12" fill="none" stroke="#ef3b24" stroke-width="1.2"/>
              <rect x="7" y="9" width="12" height="9" rx="1" fill="none" stroke="#ef3b24" stroke-width="1.2"/>
              <line x1="7" y1="12" x2="19" y2="12" stroke="#ef3b24" stroke-width="1.2"/>
            </svg>
            <p class="care-item__text">Leftovers keep well for up to five days in the fridge. Wrap each slice tightly to keep it moist and fresh.</p>
          </li>
          <li class="care-item">
            <svg class="care-item__icon" viewBox="0 0 26 26" aria-hidden="true">
              <circle cx="13" cy="13" r="12" fill="none" stroke="#ef3b24" stroke-width="1.2"/>
              <line x1="13" y1="6" x2="13" y2="20" stroke="#ef3b24" stroke-width="1.2"/>
              <line x1="7" y1="9.5" x2="19" y2="16.5" stroke="#ef3b24" stroke-width="1.2"/>
              <line x1="7" y1="16.5" x2="19" y2="9.5" stroke="#ef3b24" stroke-width="1.2"/>
            </svg>
            <p class="care-item__text">Want to save some for later? Freeze slices in an airtight bag for up to three months and thaw overnight.</p>
          </li>
          <li class="care-item">
            <svg class="care-item__icon" viewBox="0 0 26 26" aria-hidden="true">
              <circle cx="13" cy="13" r="12" fill="none" stroke="#ef3b24" stroke-width="1.2"/>
              <path d="M8 16 h10 M9 16 q4 -8 8 0" fill="none" stroke="#ef3b24" stroke-width="1.2"/>
            </svg>
            <p class="care-item__text">Warm a slice for ten seconds and add a scoop of ice cream for a cozy holiday treat.</p>
          </li>
        </ul>

        <p class="closing">Enjoy your cake by the slice!</p>
      </div>
    </div>
  </section>

</main>
</body>
</html>
```